Clear Strand Record Protocol Flyer

We need a flyer describing our initiative that seeks to develop and implement a standardized way of describing terrestrial fibre optic networks, which form the backbone of the Internet.
The primary audience that we are targeting is government and development decision makers and regulators, as well as businesses and groups involved in researching, planning, deploying and maintaining fibre optic infrastructure.

```html
<!DOCTYPE html>
<html lang="en">
<head>
<meta charset="utf-8">
<title>Clear Strand Record Protocol – Flyer</title>
<link rel="stylesheet" href="https://fonts.googleapis.com/css2?family=Michroma&family=Montserrat:wght@400;500;800&display=swap">
<style>
  :root{
    --stage:#154a72;
    --sheet-top:#2a2590;
    --sheet-bottom:#16145a;
    --band:#231f7c;
    --accent:#4ec8f4;
    --swoosh:#2f86dc;
    --text:#e6e8ff;
    --muted:#c9cdf2;
    --rule:rgba(255,255,255,.14);
  }
  *{box-sizing:border-box;margin:0;padding:0}
  html,body{width:1200px;height:800px;overflow:hidden;background:var(--stage)}
  body{position:relative;font-family:"Montserrat",sans-serif;color:var(--text)}

  .sheet{position:absolute;top:170px;width:580px;height:450px;overflow:hidden;
    background:linear-gradient(180deg,var(--sheet-top),var(--sheet-bottom));}
  .sheet--outside{left:13px}
  .sheet--inside{left:607px}

  .fold{position:absolute;top:0;bottom:0;width:1px;background:var(--rule)}

  .photo{position:absolute}
  .photo--circuit{left:0;top:0;width:580px;height:225px;
    background:radial-gradient(circle at 30% 60%,#9a7bff 0,#5a3fd0 25%,#2b2394 55%,#1b1660 100%);}
  .photo--servers{left:0;top:0;width:580px;height:110px;
    background:linear-gradient(90deg,#0f1a4a,#1c3f8a 50%,#2b6fd1 80%,#173a7e);}
  .photo--round{border-radius:50%;border:4px solid #2a2a9a}
  .photo--chip{left:-18px;top:330px;width:112px;height:112px;
    background:radial-gradient(circle,#8fb6ff,#3d5fd6 55%,#1c1f6e);}
  .photo--team{left:470px;top:330px;width:112px;height:112px;
    background:radial-gradient(circle,#9fb3c8,#4c6a8f 55%,#1e2d58);}
  .photo--data{left:215px;top:345px;width:140px;height:62px;
    background:linear-gradient(90deg,#f4f6fb 48%,#bcd9ea 52%,#9cc6de);}

  .brand{position:absolute;left:398px;top:18px;width:172px;height:70px;border-radius:35px;
    background:var(--swoosh);display:flex;align-items:center;justify-content:center;gap:10px}
  .brand__dot{width:14px;height:14px;border-radius:50%;background:#fff}
  .brand__name{font-family:"Montserrat",sans-serif;font-weight:500;font-size:34px;color:#fff;letter-spacing:1px}

  .heading{font-family:"Michroma",sans-serif;font-size:10px;letter-spacing:.5px;color:#fff;text-transform:uppercase}
  .heading--accent{color:var(--accent)}
  .band{position:absolute;left:0;top:225px;width:193px;height:40px;background:var(--band);
    display:flex;align-items:center;padding-left:18px}

  .panel{position:absolute;width:193px;padding:0 16px}
  .body{font-size:6.6px;line-height:1.45;color:var(--muted)}
  .body p+p{margin-top:7px}

  .join{font-size:11px;line-height:1.3;color:#fff}
  .url{font-size:7px;color:#fff;margin-top:24px}
  .social{width:16px;height:16px;background:#2a79c8;margin-top:8px}
  .callout{font-weight:800;font-size:11px;line-height:1.2;color:var(--accent);margin-bottom:12px}

  .caption{position:absolute;left:200px;top:410px;width:170px;font-size:4.6px;line-height:1.35;color:var(--muted)}
</style>
</head>
<body>

<!-- Outside face -->
<section class="sheet sheet--outside">
  <div class="photo photo--circuit" role="img" aria-label="Glowing fibre optic light trails over a circuit board"></div>
  <div class="brand"><span class="brand__dot"></span><span class="brand__name">csrp</span></div>
  <div class="band"><h2 class="heading">Who's involved?</h2></div>

  <div class="panel body" style="left:0;top:282px">
    <p>Established in 2022, the CSRP has been developed in collaboration with the Harbor Development Fund, Global Signal Council, the Open Network Alliance, Lantern Web Foundation, Riverline Networks, Quadrant Links, and Continental Digital Forum.</p>
    <p>The Open Network Alliance assumed a secretariat role for the standard in 2025 and is working to advance awareness and adoption of it worldwide through in-person workshops and technical assistance.</p>
  </div>

  <div class="panel" style="left:193px;top:245px">
    <p class="join">Join our community to inform policy and investment decisions that can make the Internet for everyone.</p>
    <p class="url">https://clearstrand.info</p>
    <div class="social" aria-hidden="true"></div>
  </div>

  <div class="panel" style="left:387px;top:238px">
    <p class="callout">Everyone deserves access to affordable and reliable Internet, no matter their location or circumstance.</p>
    <p class="body">Meeting this challenge requires a community working together, ideally using shared standards and data to ensure the networks they plan and build interconnect with the global Internet.</p>
  </div>

  <span class="fold" style="left:193px"></span>
  <span class="fold" style="left:387px"></span>
</section>

<!-- Inside face -->
<section class="sheet sheet--inside">
  <div class="photo photo--servers" role="img" aria-label="Data centre server racks with blue cabling"></div>

  <div class="panel" style="left:0;top:122px">
    <h2 class="heading heading--accent">What's the problem?</h2>
    <div class="body" style="margin-top:10px">
      <p>Fibre optic infrastructure forms the backbone of the Internet, underpinning all Internet access technologies, including mobile, wireless, and satellite.</p>
      <p>Despite its importance, the telecom sector and relevant government agencies often lack consistent and readily available data to help them plan, maintain, expand, and protect it. This can cause multiple problems, including unknowingly duplicating existing infrastructure, not identifying gaps or single points of failure in current infrastructure, and not being able to effectively measure the socioeconomic impact of investments in Internet infrastructure.</p>
    </div>
  </div>

  <div class="panel" style="left:193px;top:122px">
    <h2 class="heading heading--accent">How does CSRP solve this?</h2>
    <div class="body" style="margin-top:10px">
      <p>The Clear Strand Record Protocol (CSRP) is a common language for describing terrestrial fibre optic networks. It also works to establish norms among operators and regulators for information sharing regarding terrestrial fibre deployments.</p>
      <p>The standard facilitates the exchange, analysis, and visualization of fibre network data for different stakeholders, including governments, telecom providers, and researchers. By providing a consistent schema, CSRP enhances interoperability, transparency, and informed decision-making in broadband expansion and resilience efforts.</p>
    </div>
  </div>

  <div class="panel" style="left:387px;top:122px">
    <h2 class="heading heading--accent">Who benefits?</h2>
    <div class="body" style="margin-top:10px">
      <p>Governments and communication regulators can assess national network infrastructure holistically to identify gaps in infrastructure and areas of network fragility. CSRP also helps avoid duplication in reporting of fibre infrastructure where multiple operators may report fibre on a single deployment.</p>
      <p>Investors and planners can make more informed data-driven decisions on infrastructure development.</p>
      <p>Surveyors, engineers, and researchers can access standardized data through GIS tools and mapping platforms.</p>
    </div>
  </div>

  <div class="photo photo--round photo--chip" role="img" aria-label="Close-up of a glowing microchip with light trails"></div>
  <div class="photo photo--data" role="img" aria-label="Snapshot of structured network data beside a map of a national fibre network"></div>
  <p class="caption">[Caption text: On the left, a snapshot of CSRP data describing Brazil's fibre network. On the right, visualization of CSRP data.]</p>
  <div class="photo photo--round photo--team" role="img" aria-label="Professionals in discussion around a meeting table"></div>

  <span class="fold" style="left:193px"></span>
  <span class="fold" style="left:387px"></span>
</section>

</body>
</html>
```